House-share and Room Rental Website (With Focus on the Bedroom Landing Page)

Looking for website design for our House-share (executive accommodation) and room rental business.

Our company name is: Lodvenra could also be written as LodVenra or lodvenra. Either is fine .. just looking for a nice clean catchy logo to go with the design.

EXAMPLES
These are examples of other websites in this field that are doing well. this is a kind of baseline.
https://kelbrin.com.au/
https://www.tuvaplex.com/
https://www.nestorvi.com/
https://www.quillsa.net/
https://www.pendlebarrow.com.au/

Our business model is to rent rooms to people looking for high-quality accommodation. We fill the gap between those looking to rent rooms and those with rooms to rent. However, our model is slightly different from those already on the market as we looking to fill a massive gap in the market delivering upmarket rooms for rent.(Executive Accommodation) also in the back end will be coupled with a self management process in the back end.

We offer executive style accommodation that stands out above the rest. With special extras like fire safety.. and management processes that create happier homes. We are looking for a web design package that can help us grow and scale our business. We need a design that is captivating

Our MAIN focus is having a room landing page that stands out from the rest... The core of our business will rely on the promotion of the rooms in a share house... so the whole design relies on the BEDROOM landing page to drive results.

Target Market(s)

We have 2 markets we are aiming at ... the first market is people offering rooms to rent who want the highest rental return. The second market is people looking to rent safe, high-quality rooms, in houses that are well managed and looked after.

Industry/Entity Type

Share Economy

Logo Text

LodVenra

Number of Pages Required

5+ page

Font styles to use
Sans Serif

Colors
3276b5

Requirements
Must have
• A messaging system whereby we can create direct communication between those offering rooms and those looking for rooms.
• A call to action that says " Schedule an Inspection"
• Landing page for promoting rooms
• A home page for showing stock.
• Profile page for those selling rooms
• Profile page for those looking for rooms.
• A scheduling calendar for booking inspections
Nice to have
• Pages where new residents can lock in a room.. pay bond and rents.. and sign contracts
• Notifications
• SMS capabilities in the backend.
Should not have
• No script or handwriting fonts.

```html
<!DOCTYPE html>
<html lang="en">
<head>
<meta charset="utf-8">
<title>LodVenra – Find Your Ideal Room For Rent</title>
<link rel="stylesheet" href="https://fonts.googleapis.com/css2?family=Exo+2:wght@500;600;700&family=Mulish:wght@400;600;700&display=swap">
<style>
:root{
  --brand:#3276b5;
  --brand-dark:#245d93;
  --ink:#2b2b2b;
  --muted:#8a8a8a;
  --soft:#f3f3f3;
  --panel:#ececec;
  --footer:#141414;
  --white:#ffffff;
}
*{box-sizing:border-box;margin:0;padding:0}
html,body{width:1200px;height:4749px;overflow:hidden}
body{font-family:"Mulish",sans-serif;color:var(--ink);background:var(--white);position:relative}
.section-title{font-family:"Exo 2",sans-serif;font-weight:600;color:var(--brand);text-align:center;font-size:40px;letter-spacing:.5px}
.btn{display:inline-block;background:var(--brand);color:var(--white);font-family:"Mulish",sans-serif;font-weight:700;font-size:15px;text-transform:uppercase;border-radius:4px;text-align:center}

/* Hero */
.hero{position:absolute;left:0;top:0;width:1200px;height:680px;background:radial-gradient(ellipse at 55% 45%,#6d5a48 0%,#3b3029 45%,#1c1714 100%)}
.hero-shade{position:absolute;inset:0;background:rgba(0,0,0,.35)}
.nav{position:absolute;left:79px;right:76px;top:22px;height:60px;display:flex;align-items:center}
.brand{display:flex;align-items:center;gap:10px;font-family:"Exo 2",sans-serif;font-weight:600;font-size:32px;color:var(--white)}
.brand-mark{width:26px;height:26px;background:var(--brand)}
.nav-login{margin-left:auto;color:var(--white);font-size:14px;font-weight:700;margin-right:34px}
.nav .btn{padding:12px 22px;font-size:14px}
.hero-title{position:absolute;top:285px;width:100%;text-align:center;font-family:"Exo 2",sans-serif;font-weight:700;font-size:52px;color:var(--white)}
.hero-sub{position:absolute;top:348px;width:100%;text-align:center;font-size:21px;color:var(--white)}
.search{position:absolute;top:418px;left:262px;width:676px;height:50px;display:flex;gap:12px}
.search-field{flex:1;background:var(--white);border-radius:4px;font-size:13px;color:var(--muted);padding:17px 18px}
.search .btn{width:124px;padding-top:16px;font-size:15px;display:flex;align-items:center;justify-content:center;gap:7px}

/* Why use */
.why{position:absolute;top:680px;left:0;width:1200px;height:507px}
.why .section-title{position:absolute;top:58px;width:100%}
.why-item{position:absolute;top:137px;width:280px;text-align:center}
.why-item svg{display:block;margin:0 auto}
.why-item h3{font-family:"Exo 2",sans-serif;font-weight:600;font-size:20px;margin-top:28px}
.why-item p{font-size:13px;color:var(--muted);line-height:21px;margin-top:16px;padding:0 14px}
.why-item .btn{margin-top:22px;width:204px;padding:14px 0}

/* Featured */
.featured{position:absolute;top:1187px;left:0;width:1200px;height:1007px;background:var(--soft)}
.featured .section-title{position:absolute;top:55px;width:100%}
.card{position:absolute;width:323px;height:384px;background:var(--white)}
.card-photo{position:relative;height:203px}
.price{position:absolute;right:0;bottom:0;background:var(--brand);color:var(--white);font-weight:700;font-size:19px;padding:11px 12px}
.card h4{font-family:"Exo 2",sans-serif;font-weight:600;color:var(--brand);font-size:17px;margin:28px 18px 0}
.card p{font-size:13px;color:var(--muted);line-height:20px;margin:8px 18px 0}
.meta{display:flex;gap:20px;margin:26px 18px 0;font-size:12.5px;color:var(--ink)}
.meta span{display:flex;align-items:center;gap:6px}

/* Bedroom */
.bedroom{position:absolute;top:2194px;left:0;width:1200px;height:855px}
.bedroom .section-title{position:absolute;top:55px;width:100%}
.details{position:absolute;left:127px;top:203px;width:528px;height:541px;background:var(--panel);padding:60px 0 0 47px}
.details dl{display:grid;grid-template-columns:190px 1fr;row-gap:22px;font-size:15px}
.details dt{font-weight:700;color:var(--ink)}
.details dd{color:var(--brand)}
.details dd::before{content:":";color:var(--ink);margin-right:10px}
.bed-photo{position:absolute;left:655px;top:161px;width:421px;height:551px;background:linear-gradient(160deg,#5b5d61 0%,#34363a 50%,#1b1c1e 100%)}
.pager{position:absolute;top:2941px;left:558px;display:flex;gap:8px}
.pager span{width:38px;height:38px;border:2px solid #9a9a9a;border-radius:4px;display:flex;align-items:center;justify-content:center}

/* Room amenities */
.amenities-photo{position:absolute;top:3049px;left:0;width:1200px;height:681px;background:linear-gradient(100deg,#4b4540 0%,#8d8378 45%,#cfc6ba 100%)}
.amenities-panel{position:absolute;top:3153px;left:665px;width:459px;height:466px;background:rgba(240,240,240,.9);padding:56px 0 0 56px}
.amenities-panel h2{font-family:"Exo 2",sans-serif;font-weight:600;color:var(--brand);font-size:40px}
.amenities-panel ul{list-style:none;margin-top:26px}
.amenities-panel li{display:flex;align-items:center;gap:16px;font-size:15px;height:37px}

/* Public amenities */
.public{position:absolute;top:3730px;left:0;width:1200px;height:370px}
.public .section-title{position:absolute;top:66px;width:100%}
.pub-item{position:absolute;top:145px;width:200px;text-align:center;font-size:14px;color:var(--ink);line-height:20px}
.pub-item svg{display:block;margin:0 auto 26px}

/* Schedule band */
.schedule{position:absolute;top:4100px;left:0;width:1200px;height:301px;background:var(--brand);text-align:center;color:var(--white)}
.schedule h2{font-family:"Exo 2",sans-serif;font-weight:600;font-size:32px;line-height:44px;padding-top:64px}
.schedule p{font-size:14px;margin-top:14px}
.schedule .outline{display:inline-block;margin-top:26px;border:2px solid var(--white);border-radius:4px;padding:13px 30px;font-weight:700;font-size:15px}

/* Footer */
.footer{position:absolute;top:4401px;left:0;width:1200px;height:348px;background:var(--footer);color:#cfcfcf}
.footer .brand{position:absolute;left:79px;top:50px}
.footer-about{position:absolute;left:79px;top:132px;width:290px;font-size:12.5px;line-height:20px;color:#bdbdbd}
.socials{position:absolute;left:79px;top:200px;display:flex;gap:10px}
.socials span{width:40px;height:40px;border-radius:50%;background:var(--brand)}
.footer-col{position:absolute;top:60px}
.footer-col h5{font-family:"Exo 2",sans-serif;font-weight:600;color:var(--brand);font-size:15px;letter-spacing:.5px}
.footer-col ul{list-style:none;margin-top:18px}
.footer-col li{font-size:12.5px;line-height:25px;display:flex;align-items:center;gap:10px}
.footer-col li::before{content:"";width:5px;height:5px;border-radius:50%;background:var(--brand)}
.footer-rule{position:absolute;left:79px;right:76px;top:285px;height:1px;background:#2e2e2e}
.copyright{position:absolute;top:302px;width:100%;text-align:center;font-size:13px;color:#bdbdbd}
</style>
</head>
<body>

<header class="hero" role="img" aria-label="Photo of a warm hallway with two people walking through a shared house">
  <div class="hero-shade"></div>
  <nav class="nav">
    <div class="brand"><span class="brand-mark"></span>LodVenra</div>
    <span class="nav-login">LOGIN</span>
    <span class="btn">Schedule an Inspection</span>
  </nav>
  <h1 class="hero-title">Find Your Ideal Room For Rent</h1>
  <p class="hero-sub">The world's largest roommate finder</p>
  <div class="search">
    <div class="search-field">Where Do You Want To live ?</div>
    <span class="btn"><svg width="14" height="14" viewBox="0 0 14 14" fill="none" stroke="#fff" stroke-width="2"><circle cx="6" cy="6" r="4.5"/><path d="M9.5 9.5L13 13"/></svg>Search</span>
  </div>
</header>

<section class="why">
  <h2 class="section-title">WHY USE LodVenra</h2>
  <div class="why-item" style="left:108px">
    <svg width="110" height="108" viewBox="0 0 110 108" fill="none" stroke="#3276b5" stroke-width="2.5"><rect x="12" y="10" width="84" height="88" fill="#e9f1f9"/><path d="M22 20h64v68H22zM22 50h30v38M52 20v20M66 50h20M66 50v20"/></svg>
    <h3>Find Your Room</h3>
    <p>Lorem Ipsum is simply dummy text of the printing and typesetting industry. Lorem Ipsum has been the.</p>
    <span class="btn">Looking for Rooms</span>
  </div>
  <div class="why-item" style="left:460px">
    <svg width="110" height="108" viewBox="0 0 110 108" fill="none" stroke="#3276b5" stroke-width="2.5"><rect x="14" y="8" width="82" height="92" fill="#e9f1f9"/><path d="M24 28h62v62H24zM55 28v62M24 18h62"/><circle cx="42" cy="50" r="5"/><circle cx="68" cy="50" r="5"/></svg>
    <h3>Selling Rooms</h3>
    <p>Lorem Ipsum is simply dummy text of the printing and typesetting industry. Lorem Ipsum has been the.</p>
    <span class="btn">Selling Rooms</span>
  </div>
  <div class="why-item" style="left:810px">
    <svg width="110" height="108" viewBox="0 0 110 108" fill="none" stroke="#3276b5" stroke-width="2.5"><path d="M14 14h82v62H44l-20 18V76H14z" fill="#e9f1f9"/><circle cx="38" cy="45" r="4" fill="#3276b5"/><circle cx="55" cy="45" r="4" fill="#3276b5"/><circle cx="72" cy="45" r="4" fill="#3276b5"/></svg>
    <h3>We're here to help</h3>
    <p>Lorem Ipsum is simply dummy text of the printing and typesetting industry. Lorem Ipsum has been the.</p>
    <span class="btn">Contact Us</span>
  </div>
</section>

<section class="featured">
  <h2 class="section-title">FEATURED LISTING</h2>

  <article class="card" style="left:79px;top:130px">
    <div class="card-photo" role="img" aria-label="Photo of a grey living room with a rug and armchairs" style="background:linear-gradient(135deg,#6b6d6f,#9c9790)"><span class="price">$299,000</span></div>
    <h4>PROPERTY ADDRESS</h4>
    <p>Lorem Ipsum is simply dummy text of the printing and typesetting</p>
    <div class="meta"><span>⤡ 1,962 sq ft</span><span>▭ 3 beds</span><span>◌ 2 baths</span></div>
  </article>
  <article class="card" style="left:440px;top:130px">
    <div class="card-photo" role="img" aria-label="Photo of a bright lounge with a dark sofa" style="background:linear-gradient(135deg,#3c3a38,#b9b3aa)"><span class="price">$299,000</span></div>
    <h4>PROPERTY ADDRESS</h4>
    <p>Lorem Ipsum is simply dummy text of the printing and typesetting</p>
    <div class="meta"><span>⤡ 1,962 sq ft</span><span>▭ 3 beds</span><span>◌ 3 baths</span></div>
  </article>
  <article class="card" style="left:801px;top:130px">
    <div class="card-photo" role="img" aria-label="Photo of a bedroom with deep red walls" style="background:linear-gradient(135deg,#5a1e22,#a9a29a)"><span class="price">$299,000</span></div>
    <h4>PROPERTY ADDRESS</h4>
    <p>Lorem Ipsum is simply dummy text of the printing and typesetting</p>
    <div class="meta"><span>⤡ 1,962 sq ft</span><span>▭ 3 beds</span><span>◌ 1 baths</span></div>
  </article>
  <article class="card" style="left:79px;top:561px">
    <div class="card-photo" role="img" aria-label="Photo of a media room with a large screen and wood panelling" style="background:linear-gradient(135deg,#6e4b2e,#3a3028)"><span class="price">$299,000</span></div>
    <h4>PROPERTY ADDRESS</h4>
    <p>Lorem Ipsum is simply dummy text of the printing and typesetting</p>
    <div class="meta"><span>⤡ 1,962 sq ft</span><span>▭ 3 beds</span><span>◌ 2 baths</span></div>
  </article>
  <article class="card" style="left:440px;top:561px">
    <div class="card-photo" role="img" aria-label="Photo of a modern open-plan living area with tall windows" style="background:linear-gradient(135deg,#8f8e8c,#d6d4d0)"><span class="price">$299,000</span></div>
    <h4>PROPERTY ADDRESS</h4>
    <p>Lorem Ipsum is simply dummy text of the printing and typesetting</p>
    <div class="meta"><span>⤡ 1,962 sq ft</span><span>▭ 3 beds</span><span>◌ 3 baths</span></div>
  </article>
  <article class="card" style="left:801px;top:561px">
    <div class="card-photo" role="img" aria-label="Photo of a light lounge with a fireplace" style="background:linear-gradient(135deg,#b5b2a8,#e6e3dc)"><span class="price">$299,000</span></div>
    <h4>PROPERTY ADDRESS</h4>
    <p>Lorem Ipsum is simply dummy text of the printing and typesetting</p>
    <div class="meta"><span>⤡ 1,962 sq ft</span><span>▭ 3 beds</span><span>◌ 1 baths</span></div>
  </article>
</section>

<section class="bedroom">
  <h2 class="section-title">BEDROOM</h2>
  <div class="details">
    <dl>
      <dt>Gender Preference</dt><dd>Male/female/single/couple</dd>
      <dt>Size of room</dt><dd>Sqm</dd>
      <dt>Bathroom</dt><dd>Shared/private</dd>
      <dt>Parking</dt><dd>Street/off-street/private</dd>
      <dt>Minimum contract ter</dt><dd>usually 3 months</dd>
      <dt>Bed size</dt><dd>Ft</dd>
      <dt>Type of housemates</dt><dd>Professionals/students</dd>
      <dt>Room type</dt><dd>Private/shared</dd>
      <dt>Internet speed</dt><dd>Put</dd>
    </dl>
  </div>
  <div class="bed-photo" role="img" aria-label="Photo of a dark modern bedroom with a low bed and lit headboard"></div>
</section>
<div class="pager">
  <span><svg width="10" height="14" viewBox="0 0 10 14" fill="none" stroke="#3276b5" stroke-width="2.5"><path d="M8 1L2 7l6 6"/></svg></span>
  <span><svg width="10" height="14" viewBox="0 0 10 14" fill="none" stroke="#3276b5" stroke-width="2.5"><path d="M2 1l6 6-6 6"/></svg></span>
</div>

<section class="amenities-photo" role="img" aria-label="Photo of a bedside table with a lamp and glass vases beside soft curtains"></section>
<div class="amenities-panel">
  <h2>ROOM AMENITIES</h2>
  <ul>
    <li><svg width="18" height="18" viewBox="0 0 18 18" fill="none" stroke="#3276b5" stroke-width="2"><circle cx="9" cy="9" r="7.5"/><path d="M5.5 9.2l2.3 2.3 4.7-4.8"/></svg>Furnished/unfurnished</li>
    <li><svg width="18" height="18" viewBox="0 0 18 18" fill="none" stroke="#3276b5" stroke-width="2"><circle cx="9" cy="9" r="7.5"/><path d="M5.5 9.2l2.3 2.3 4.7-4.8"/></svg>TV</li>
    <li><svg width="18" height="18" viewBox="0 0 18 18" fill="none" stroke="#3276b5" stroke-width="2"><circle cx="9" cy="9" r="7.5"/><path d="M5.5 9.2l2.3 2.3 4.7-4.8"/></svg>Storage space</li>
    <li><svg width="18" height="18" viewBox="0 0 18 18" fill="none" stroke="#3276b5" stroke-width="2"><circle cx="9" cy="9" r="7.5"/><path d="M5.5 9.2l2.3 2.3 4.7-4.8"/></svg>Study Desk / Workstation</li>
    <li><svg width="18" height="18" viewBox="0 0 18 18" fill="none" stroke="#3276b5" stroke-width="2"><circle cx="9" cy="9" r="7.5"/><path d="M5.5 9.2l2.3 2.3 4.7-4.8"/></svg>Wardrobe</li>
    <li><svg width="18" height="18" viewBox="0 0 18 18" fill="none" stroke="#3276b5" stroke-width="2"><circle cx="9" cy="9" r="7.5"/><path d="M5.5 9.2l2.3 2.3 4.7-4.8"/></svg>Ensuite shower</li>
    <li><svg width="18" height="18" viewBox="0 0 18 18" fill="none" stroke="#3276b5" stroke-width="2"><circle cx="9" cy="9" r="7.5"/><path d="M5.5 9.2l2.3 2.3 4.7-4.8"/></svg>Kitchenette</li>
  </ul>
</div>

<section class="public">
  <h2 class="section-title">PUBLIC AMENITIES</h2>
  <div class="pub-item" style="left:80px">
    <svg width="56" height="80" viewBox="0 0 56 80" fill="none" stroke="#3276b5" stroke-width="2.5"><path d="M6 4h44v28a6 6 0 000 12v32H6V44a6 6 0 000-12z"/><path d="M16 54h24M16 62h16"/></svg>
    Transport options</div>
  <div class="pub-item" style="left:287px">
    <svg width="60" height="80" viewBox="0 0 60 80" fill="none" stroke="#3276b5" stroke-width="2.5"><rect x="6" y="4" width="48" height="60" rx="10"/><path d="M6 36h48M14 78l8-14M46 78l-8-14"/><circle cx="18" cy="50" r="3"/><circle cx="42" cy="50" r="3"/></svg>
    Trains</div>
  <div class="pub-item" style="left:497px">
    <svg width="60" height="80" viewBox="0 0 60 80" fill="none" stroke="#3276b5" stroke-width="2.5"><rect x="6" y="8" width="48" height="60" rx="6"/><path d="M6 40h48M12 68v8M48 68v8M20 8V2h20v6"/><circle cx="18" cy="54" r="3"/><circle cx="42" cy="54" r="3"/></svg>
    Busses</div>
  <div class="pub-item" style="left:700px">
    <svg width="100" height="80" viewBox="0 0 100 80" fill="none" stroke="#3276b5" stroke-width="2.5"><path d="M18 60c-8-12-12-18-12-24a12 12 0 0124 0c0 6-4 12-12 24z"/><circle cx="18" cy="36" r="4"/><path d="M50 76V30h18V4h14v72M50 76h46M56 40h6M56 52h6M72 16h6M72 30h6M72 44h6"/></svg>
    Location or<br>Distance to the City</div>
  <div class="pub-item" style="left:927px">
    <svg width="80" height="80" viewBox="0 0 80 80" fill="none" stroke="#3276b5" stroke-width="2.5"><path d="M4 36l22-8 28 8 22-8v46l-22 8-28-8-22 8z"/><path d="M26 28v46M54 36v46"/><path d="M54 30c-7-9-10-14-10-19a10 10 0 0120 0c0 5-3 10-10 19z"/><circle cx="54" cy="11" r="3"/></svg>
    MAP of the area and<br>shortest route to the city.</div>
</section>

<section class="schedule">
  <h2>SCHEDULING CALENDAR FOR BOOKING<br>INSPECTIONS</h2>
  <p>Lorem Ipsum is simply dummy text of the printing and typesetting industry. Lorem Ipsum has been the.</p>
  <span class="outline">VIEW CALENDAR</span>
</section>

<footer class="footer">
  <div class="brand"><span class="brand-mark"></span>LodVenra</div>
  <p class="footer-about">Lorem Ipsum is simply dummy text of the printing and typesetting industr Lorem Ipsum.</p>
  <div class="socials"><span></span><span></span><span></span></div>
  <div class="footer-col" style="left:434px">
    <h5>QUICK LINKS</h5>
    <ul><li>Sign up</li><li>Log in</li><li>Pricing</li><li>Privacy Policy</li><li>Contact Us</li><li>Terms of use</li></ul>
  </div>
  <div class="footer-col" style="left:792px">
    <h5>PREVIEW HOUSE SHARE</h5>
    <ul><li>Lorem ipsum simple text of print</li><li>Ipsum simple text of print</li><li>Room simple</li><li>Lorem ipsum simple text of print</li><li>Ipsum simple text</li><li>Lorem ipsum simple print</li></ul>
  </div>
  <div class="footer-rule"></div>
  <p class="copyright">©LodVenra - 2019 All Right Reserved.</p>
</footer>

</body>
</html>
```